LEARN Business Skills so you can Earn a good living

size of the poster is 8”x 10.75" plus 0.25" bleed.
Please leave 1 inch on the bottoum for footer
I want a design a poster that will attract people's attention.
I appreciate a creative ad however the ad should not take away from being able to clearly read the text.
-I also appreciate a simple creative ad that is not too busy.
-you can use graphics, vectors, or pictures of real people.
-however, if you use real people it should be a white male that is wearing a white shirt and look like a professional person.

Target Market(s)

Potential young business people

Industry/Entity Type

education

Requirements
Must have
• easy to read the text
Nice to have
• I would like a "creative" simple ad that is easy to be read
Should not have
• pictures of women

```html
<!DOCTYPE html>
<html lang="en">
<head>
<meta charset="utf-8">
<title>Learn It to Earn It – Business Enrichment Course</title>
<link rel="stylesheet" href="https://fonts.googleapis.com/css2?family=Montserrat:wght@300;400;700;800;900&family=Great+Vibes&display=swap">
<style>
  :root {
    --backdrop: #8e8e8e;
    --ink-dark: #29292b;
    --band-mid: #5f6061;
    --band-low: #2c2c2e;
    --paper: #ffffff;
    --photo-light: #e9e6e3;
    --photo-warm: #c9a58c;
    --photo-dark: #3a3a3b;
  }
  html, body {
    margin: 0;
    padding: 0;
    width: 1200px;
    height: 1200px;
    overflow: hidden;
    background: var(--backdrop);
  }
  .poster {
    position: absolute;
    left: 176px;
    top: 40px;
    width: 847px;
    height: 1120px;
    display: block;
  }
  .headline {
    font-family: 'Montserrat', sans-serif;
    font-weight: 900;
    fill: var(--paper);
    filter: drop-shadow(0 14px 10px rgba(0,0,0,0.45));
  }
  .headline-script {
    font-family: 'Great Vibes', cursive;
    fill: var(--paper);
    filter: drop-shadow(0 10px 8px rgba(0,0,0,0.45));
  }
  .course-title {
    font-family: 'Montserrat', sans-serif;
    font-weight: 700;
    font-size: 68px;
    fill: var(--paper);
  }
  .course-tagline {
    font-family: 'Montserrat', sans-serif;
    font-weight: 400;
    font-size: 22px;
    fill: var(--paper);
  }
  .benefits {
    font-family: 'Montserrat', sans-serif;
    font-weight: 700;
    font-size: 43px;
    fill: var(--paper);
  }
  .topics {
    font-family: 'Montserrat', sans-serif;
    font-weight: 700;
    font-size: 15.5px;
    fill: var(--paper);
  }
</style>
</head>
<body>
<svg class="poster" viewBox="0 0 1268 1677" xmlns="http://www.w3.org/2000/svg">
  <defs>
    <linearGradient id="lower-band" x1="0" y1="0" x2="0" y2="1">
      <stop offset="0" stop-color="#4f5051"/>
      <stop offset="0.45" stop-color="var(--band-mid)"/>
      <stop offset="1" stop-color="var(--band-low)"/>
    </linearGradient>
    <radialGradient id="portrait-tones" cx="0.5" cy="0.6" r="0.6">
      <stop offset="0" stop-color="var(--photo-light)"/>
      <stop offset="0.55" stop-color="#d8cfc8"/>
      <stop offset="0.8" stop-color="var(--photo-warm)" stop-opacity="0.6"/>
      <stop offset="1" stop-color="var(--photo-dark)" stop-opacity="0"/>
    </radialGradient>
  </defs>

  <rect class="band-top" x="0" y="0" width="1268" height="760" fill="var(--ink-dark)"/>
  <rect class="band-lower" x="0" y="760" width="1268" height="767" fill="url(#lower-band)"/>
  <rect class="footer-space" x="0" y="1527" width="1268" height="150" fill="var(--paper)"/>

  <rect class="hero-portrait" x="340" y="50" width="600" height="710" rx="180"
        fill="url(#portrait-tones)" role="img"
        aria-label="Smiling young businessman in a white shirt holding a phone and a bank card"/>

  <text class="headline" x="135" y="760" font-size="217" textLength="1013" lengthAdjust="spacingAndGlyphs">LEARN IT</text>
  <text class="headline-script" x="120" y="951" font-size="160">to</text>
  <text class="headline" x="260" y="951" font-size="217" textLength="888" lengthAdjust="spacingAndGlyphs">EARN IT</text>

  <g class="course-block" text-anchor="end">
    <text class="course-title" x="573" y="1076">Business</text>
    <text class="course-title" x="573" y="1143">Enrichment</text>
    <text class="course-title" x="573" y="1210">Course</text>
    <text class="course-tagline" x="573" y="1255">A proven success of helping people</text>
  </g>

  <g class="benefit-block">
    <text class="benefits" x="688" y="1070">Get a quality job -</text>
    <text class="benefits" x="688" y="1128">start / grow your</text>
    <text class="benefits" x="688" y="1186">business-Increase</text>
    <text class="benefits" x="688" y="1246">your salary</text>
  </g>

  <g class="topic-list">
    <text class="topics" x="120" y="1365">BUSINESS ADMIISTRATION - SMALL BUSINESS MANAGEMENT -</text>
    <text class="topics" x="120" y="1393">FINANCE - INVESTMENTS - COMPUTERS- ACCOUNTING - SALES  MARKETING - PROJECT MANAGEMENT INTERVIEWING</text>
    <text class="topics" x="120" y="1421">SKILLS - BUSINESS LAW -NEGOTIATION - PUBLIC SPEAKING - IMPORT/EXPORT - INFORMATION TECHNOLOY -</text>
    <text class="topics" x="120" y="1449">DISTRIBUTION - MARKETING  -   LEDGERLY - REAL ESTATE - HEALTH CARE-MANAGEMENT - SHOPVALE</text>
  </g>
</svg>
</body>
</html>
```